Flyer overhaul from current flyers

I need to have our current flyers updated with a fresher look. We also need to have a new utility and real estate flyer created that will go along with the design of the new flyer. We are looking for new pictures, new overall design, same color scheme but would like to have the flyers more airy and inviting.

Target Market(s)

decision makers in the healthcare/utilty/banking/real estate sectors

Font styles to use
Other font styles liked:
• Logo is in Bell MT

Colors
0054AA
0677BA
7BADD7
CADEEF
E8F1F8

Requirements
Must have
• Close to what is currently on the existing flyers

```html
<!DOCTYPE html>
<html lang="en">
<head>
<meta charset="utf-8">
<title>Harbor Ridge Recovery – Flyers</title>
<link href="https://fonts.googleapis.com/css2?family=Montserrat:wght@400;500;600;700&family=Roboto+Condensed:wght@400;500&display=swap" rel="stylesheet">
<style>
  :root{
    --page:#d0e3ee;
    --navy:#0b5576;
    --navy-deep:#094764;
    --cyan:#3fb6e6;
    --cyan-bright:#12b0e8;
    --charcoal:#3e4447;
    --charcoal-dark:#33383b;
    --white:#ffffff;
    --photo-gray:#8d98a3;
  }
  *{margin:0;padding:0;box-sizing:border-box}
  html,body{width:1200px;height:802px;overflow:hidden;background:var(--page)}
  body{position:relative;font-family:"Montserrat",sans-serif;color:var(--white)}
  .flyer{position:absolute;top:53px;width:520px;height:672px;overflow:hidden}
  .flyer--services{left:71px;background:var(--navy)}
  .flyer--philosophy{left:607px;background:var(--charcoal)}
  .abs{position:absolute}

  /* Services flyer */
  .hero-art{left:0;top:0;width:520px;height:300px}
  .brand{display:flex;align-items:center;gap:9px}
  .brand-dot{width:46px;height:46px;border-radius:50%;background:var(--cyan-bright);flex:none}
  .brand-name{font-family:"Montserrat",sans-serif;font-weight:600;font-size:15px;line-height:1.1;letter-spacing:.04em;color:var(--white)}
  .brand--top{left:31px;top:35px}
  .title{left:31px;top:290px;font-weight:700;font-size:43px;line-height:43px;letter-spacing:-.2px}
  .subhead{font-weight:700;font-size:16.5px;line-height:19px;color:var(--cyan)}
  .subhead--left{left:31px;top:383px}
  .subhead--right{left:282px;top:383px}
  .col-divider{left:259px;top:389px;width:1px;height:207px;background:var(--cyan);opacity:.7}
  .list{list-style:none;font-family:"Roboto Condensed",sans-serif;font-size:10.5px}
  .checks{left:31px;top:433px}
  .checks li{height:21.7px;display:flex;align-items:center;gap:6px}
  .checks svg{width:10px;height:10px;flex:none}
  .bullets{left:282px;top:428px}
  .bullets li{height:17.4px;display:flex;align-items:center;gap:9px;padding-left:9px}
  .bullets li::before{content:"";width:3.5px;height:3.5px;border-radius:50%;background:var(--white);flex:none}
  .call-label{left:35px;width:200px;top:593px;text-align:center;font-weight:500;font-size:15px;letter-spacing:.02em}
  .contact-bar{left:0;top:615px;width:520px;height:57px;background:var(--charcoal)}
  .phone{font-weight:700;font-size:21.5px;letter-spacing:.3px}
  .pipe{width:5px;height:17px;border-radius:3px;background:var(--cyan-bright)}
  .web{font-weight:500;font-size:12.5px;letter-spacing:.2px}

  /* Philosophy flyer */
  .handshake{left:0;top:0;width:520px;height:672px}
  .statement-box{left:71px;top:260px;width:376px;height:290px;background:linear-gradient(180deg,rgba(18,176,232,.88) 0%,rgba(10,150,200,.75) 45%,rgba(62,68,71,.6) 80%,rgba(62,68,71,0) 100%)}
  .statement-title{left:71px;top:290px;width:376px;text-align:center;font-weight:500;font-size:40px;letter-spacing:.3px}
  .statement-copy{left:103px;top:345px;width:326px;font-family:"Roboto Condensed",sans-serif;font-size:12.1px;line-height:15.35px}
  .brand--bottom{left:162px;top:532px}
  .rule-row{left:69px;top:604px;width:379px;display:flex;align-items:center;gap:8px;font-weight:500;font-size:12.5px}
  .rule-row span.rule{flex:1;height:1px;background:#cfd5d8}
  .contact-row{display:flex;align-items:center}
</style>
</head>
<body>

<section class="flyer flyer--services">
  <svg class="abs hero-art" viewBox="0 0 520 300" role="img" aria-label="Photo of colleagues reviewing printed charts beside a laptop">
    <defs>
      <linearGradient id="heroPhoto" x1="0" y1="0" x2="1" y2="1">
        <stop offset="0" stop-color="#4a5258"/>
        <stop offset=".45" stop-color="#6f7f92"/>
        <stop offset=".75" stop-color="#c9ced6"/>
        <stop offset="1" stop-color="#e8eaee"/>
      </linearGradient>
    </defs>
    <path d="M0 0H520V250C430 305 250 305 110 255 60 235 20 205 0 180Z" fill="url(#heroPhoto)"/>
    <path d="M0 145C60 225 190 290 330 292 420 294 480 275 520 250V270C470 300 390 312 300 310 170 305 70 250 0 190Z" fill="#0f7fb2"/>
    <path d="M0 180C20 205 60 235 110 255 250 305 430 305 520 250V262C430 318 240 318 100 265 55 247 20 220 0 196Z" fill="#2a2f33"/>
  </svg>

  <div class="abs brand brand--top">
    <span class="brand-dot"></span>
    <span class="brand-name">HARBOR RIDGE<br>RECOVERY</span>
  </div>

  <h1 class="abs title">Financial<br>Collections</h1>

  <h2 class="abs subhead subhead--left">A Forward Thinking<br>Approach</h2>
  <h2 class="abs subhead subhead--right">An Impactful, All-In-One<br>Solution</h2>
  <div class="abs col-divider"></div>

  <ul class="abs list checks">
    <li><svg viewBox="0 0 10 10"><path d="M1 5.5L4 8.5 9 1.5" fill="none" stroke="#fff" stroke-width="1.8"/></svg>Consumer Friendly, Professional Approach</li>
    <li><svg viewBox="0 0 10 10"><path d="M1 5.5L4 8.5 9 1.5" fill="none" stroke="#fff" stroke-width="1.8"/></svg>Online Consumer Debt Negotiation Tools</li>
    <li><svg viewBox="0 0 10 10"><path d="M1 5.5L4 8.5 9 1.5" fill="none" stroke="#fff" stroke-width="1.8"/></svg>Live Online Agent Chat Portals</li>
    <li><svg viewBox="0 0 10 10"><path d="M1 5.5L4 8.5 9 1.5" fill="none" stroke="#fff" stroke-width="1.8"/></svg>Online Consumer Dispute/Complaint Tools</li>
    <li><svg viewBox="0 0 10 10"><path d="M1 5.5L4 8.5 9 1.5" fill="none" stroke="#fff" stroke-width="1.8"/></svg>FISMA Compliant Physical and Virtual Security</li>
  </ul>

  <ul class="abs list bullets">
    <li>Credit Report Monitoring</li>
    <li>Address/Phone Scrubbing</li>
    <li>Compliant Collection Letters</li>
    <li>Discretionary Credit Reporting</li>
    <li>Customizable Collection Workflow</li>
    <li>Professional Skip Tracing</li>
    <li>Deceased/Probate Services</li>
    <li>Call Recording and Monitoring</li>
    <li>Bankruptcy Claim Services</li>
    <li>Legal Collection Services</li>
  </ul>

  <p class="abs call-label">CALL US AT</p>
  <div class="abs contact-bar">
    <span class="abs phone" style="left:49px;top:14px">(555) 014-2273</span>
    <span class="abs pipe" style="left:257px;top:20px"></span>
    <span class="abs web" style="left:287px;top:20px">harborridgerecovery.com</span>
  </div>
</section>

<section class="flyer flyer--philosophy">
  <svg class="abs handshake" viewBox="0 0 520 672" role="img" aria-label="Photo of two business people shaking hands">
    <defs>
      <linearGradient id="shakePhoto" x1="0" y1="0" x2="0" y2="1">
        <stop offset="0" stop-color="#7d9dbd"/>
        <stop offset=".25" stop-color="#4d6077"/>
        <stop offset=".5" stop-color="#2b4a5f"/>
        <stop offset=".75" stop-color="#3e4447"/>
        <stop offset="1" stop-color="#3e4447"/>
      </linearGradient>
      <radialGradient id="handsGlow" cx=".45" cy=".3" r=".35">
        <stop offset="0" stop-color="#a37a60" stop-opacity=".55"/>
        <stop offset="1" stop-color="#a37a60" stop-opacity="0"/>
      </radialGradient>
    </defs>
    <rect width="520" height="672" fill="url(#shakePhoto)"/>
    <rect width="520" height="400" fill="url(#handsGlow)"/>
  </svg>

  <div class="abs statement-box"></div>
  <h1 class="abs statement-title">Our Philosophy</h1>
  <p class="abs statement-copy">For over 30 years, Harbor Ridge Recovery has assisted banks and financial services companies in the reconciliation of their past due accounts. Our philosophy is to provide consistent performance by investing in our clients’ accounts to ensure the maximum liquidation. By building on historically proven collection techniques and employing an ever-expanding access to data and technology, our agency has continued to improve our performance to the benefit of our clients. Our capital forward, compliance centered approach has proven to deliver the most consistent results for our financial service providers.</p>

  <div class="abs brand brand--bottom">
    <span class="brand-dot"></span>
    <span class="brand-name">HARBOR RIDGE<br>RECOVERY</span>
  </div>

  <div class="abs rule-row"><span class="rule"></span>CALL US AT<span class="rule"></span></div>
  <span class="abs phone" style="left:71px;top:623px">(555) 014-2273</span>
  <span class="abs pipe" style="left:263px;top:627px"></span>
  <span class="abs web" style="left:280px;top:627px">harborridgerecovery.com</span>
</section>

</body>
</html>
```